Verdant Pathworks Business Card

want the back of card to be blue- with the logo in the center
front of card- info plus logo (info being mailing address, email address, and website address )
4 different names with titles to have on cards
1) Dominic Ashvale - Owner
2) Bethany Korvuth- Customer Relationship Specialist
3) Luca Brennwick- Vice President of Sales
4) Neil Umbright- Chief Technology Officer

Target Market(s)

tech company in the government/probation office industry

Industry/Entity Type

Government Office

Contact Information for Business Card

1) Dominic Ashvale - Owner

Colors
0355a3
ffffff

Requirements
Must have
• back side should be blue, with the logo placed in the center
• front side needs to include both the logo, as well as company info (info should include website address, email address, and mailing address)

```html
<!DOCTYPE html>
<html lang="en">
<head>
<meta charset="utf-8">
<title>Verdant Pathworks Business Card</title>
<link href="https://fonts.googleapis.com/css2?family=Cinzel:wght@700&family=Lato:wght@400&display=swap" rel="stylesheet">
<style>
  :root {
    --navy: #1b2f57;
    --silver: #c7c9cc;
    --white: #ffffff;
    --ink: #3a3a3a;
    --rule-light: #8f9bb3;
    --rule-dark: #8a8a8a;
    --backdrop: #ecebe8;
  }
  html, body {
    margin: 0;
    padding: 0;
    width: 1200px;
    height: 900px;
    overflow: hidden;
    background: var(--backdrop);
  }
  .canvas {
    position: relative;
    width: 1200px;
    height: 900px;
  }
  .card {
    position: absolute;
    box-shadow: 3px 4px 6px rgba(0,0,0,0.25);
  }
  .card--back {
    left: 330px; top: 90px; width: 555px; height: 343px;
    background: var(--navy);
    color: var(--white);
  }
  .card--front {
    left: 330px; top: 469px; width: 559px; height: 343px;
    background: var(--white);
  }
  .brand {
    position: absolute;
    left: 0; right: 0;
    display: flex;
    justify-content: center;
    align-items: center;
    gap: 14px;
    font-family: "Cinzel", serif;
    font-weight: 700;
    font-size: 30px;
    letter-spacing: 1px;
    white-space: nowrap;
  }
  .brand__mark {
    width: 16px; height: 16px; border-radius: 50%;
  }
  .card--back .brand { top: 80px; color: var(--silver); }
  .card--back .brand__mark { background: var(--silver); }
  .card--front .brand { top: 150px; color: var(--navy); }
  .card--front .brand__mark { background: var(--navy); }

  .staff {
    position: absolute;
    left: 41px; top: 183px;
    width: 480px;
    display: grid;
    grid-template-columns: 235px 245px;
    row-gap: 18px;
  }
  .person__name {
    font-family: "Cinzel", serif;
    font-weight: 700;
    font-size: 20px;
    line-height: 22px;
    letter-spacing: 0.3px;
    white-space: nowrap;
  }
  .person__title {
    font-family: "Lato", sans-serif;
    font-size: 16px;
    line-height: 19px;
    white-space: nowrap;
  }
  .rule {
    position: absolute;
    height: 1px;
  }
  .card--back .rule { left: 41px; width: 472px; top: 292px; background: var(--rule-light); }
  .card--front .rule { left: 116px; width: 327px; top: 279px; background: var(--rule-dark); }
  .contact {
    position: absolute;
    left: 0; right: 0;
    text-align: center;
    font-family: "Lato", sans-serif;
    font-size: 16.5px;
    white-space: nowrap;
  }
  .card--back .contact { top: 299px; }
  .card--front .contact { top: 289px; color: var(--ink); }
</style>
</head>
<body>
<div class="canvas">
  <section class="card card--back">
    <div class="brand"><span class="brand__mark"></span>Verdant Pathworks</div>
    <div class="staff">
      <div class="person"><div class="person__name">Dominic Ashvale</div><div class="person__title">Owner</div></div>
      <div class="person"><div class="person__name">Bethany Korvuth</div><div class="person__title">Customer Relationship Specialist</div></div>
      <div class="person"><div class="person__name">Luca Brennwick</div><div class="person__title">Vice President of Sales</div></div>
      <div class="person"><div class="person__name">Neil Umbright</div><div class="person__title">Chief Technology Officer</div></div>
    </div>
    <div class="rule"></div>
    <div class="contact">support@VerdantPathworks.com &nbsp;|&nbsp; www.VerdantPathworks.com</div>
  </section>

  <section class="card card--front">
    <div class="brand"><span class="brand__mark"></span>Verdant Pathworks</div>
    <div class="rule"></div>
    <div class="contact">421, Address line here, 45452,Country Name</div>
  </section>
</div>
</body>
</html>
```